transgender support group needs innovative business card and logo

we are a transgender support group looking for a new logo and business card. I would like to include a Mona Lisa head (our logo), over top of, or somehow incorporate a rainbow (an LGBT symbol) arcing over the lower left third of the card, allowing for the text on the remaining part. Other designs are welcome, as this is just some guidance to start. I would like "MERIDAN" to possibly be larger the the "education association", and under that, I would like "a transgender resource" We also need room for the address, website and phone number. A bit larger, would need to be a spot for a name and title.
Meridian Learning Association, 412 Pine Hollow mill rd. Ashford ne18532 suite 346. phone 208 555 0147 contact person Marlene Osterby, president

```html
<!DOCTYPE html>
<html lang="en">
<head>
<meta charset="utf-8">
<title>Meridian Learning Association – Business Card</title>
<link href="https://fonts.googleapis.com/css2?family=Open+Sans:ital,wght@0,400;0,600;0,700;1,600;1,700&display=swap" rel="stylesheet">
<style>
  :root {
    --page-bg: #d8d3cb;
    --band-black: #0b0b0b;
    --card-light: #f4f3f0;
    --card-mid: #e4e2dc;
    --card-gold: #ead087;
    --ink: #1c1c1c;
    --ink-soft: #2e2e2e;
    --white: #ffffff;
    --portrait-a: #6f6a3c;
    --portrait-b: #a58a4e;
    --portrait-c: #3b3420;
  }
  * { margin: 0; padding: 0; box-sizing: border-box; }
  html, body { width: 1200px; height: 892px; overflow: hidden; }
  body {
    background: var(--page-bg);
    font-family: "Open Sans", Arial, sans-serif;
    position: relative;
  }
  .business-card {
    position: absolute;
    left: 100px;
    top: 160px;
    width: 1000px;
    height: 572px;
    overflow: hidden;
    border-radius: 6px;
    background: linear-gradient(20deg, var(--card-gold) 0%, #efdba6 30%, var(--card-mid) 62%, var(--card-light) 100%);
    box-shadow: 0 8px 24px rgba(0,0,0,0.25);
  }
  .header-band {
    position: absolute;
    left: 0; top: 0;
    width: 1000px; height: 300px;
  }
  .portrait-frame {
    position: absolute;
    left: 62px;
    top: 40px;
    width: 200px;
    height: 200px;
    transform: rotate(38deg);
    border: 7px solid var(--white);
    border-radius: 10px;
    background: radial-gradient(circle at 48% 38%, var(--portrait-b) 0%, var(--portrait-a) 45%, var(--portrait-c) 100%);
    box-shadow: 0 4px 10px rgba(0,0,0,0.35);
  }
  .org-name {
    position: absolute;
    left: 380px;
    top: 52px;
    color: var(--white);
    font-weight: 700;
    font-size: 48px;
    line-height: 1.15;
    letter-spacing: 0.5px;
  }
  .org-tagline {
    position: absolute;
    left: 380px;
    top: 204px;
    color: var(--ink-soft);
    font-weight: 600;
    font-size: 28px;
  }
  .contact-person {
    position: absolute;
    right: 60px;
    top: 300px;
    text-align: right;
    color: var(--ink);
  }
  .contact-person .person-name {
    font-weight: 700;
    font-style: italic;
    font-size: 34px;
    line-height: 1.1;
  }
  .contact-person .person-title {
    font-weight: 600;
    font-style: italic;
    font-size: 22px;
  }
  .contact-line {
    position: absolute;
    right: 40px;
    display: flex;
    align-items: center;
    gap: 14px;
    color: var(--ink);
    font-weight: 700;
    font-size: 32px;
    white-space: nowrap;
  }
  .contact-line.phone { top: 418px; }
  .contact-line.address { top: 482px; }
  .contact-icon {
    width: 28px; height: 28px;
    flex: none;
  }
</style>
</head>
<body>
  <div class="business-card">
    <svg class="header-band" viewBox="0 0 1000 300" aria-hidden="true">
      <polygon points="0,0 1000,0 1000,250 0,155" fill="var(--band-black)"/>
    </svg>

    <div class="portrait-frame" role="img" aria-label="Renaissance portrait logo of the association"></div>

    <div class="org-name">Meridian Learning<br>Association</div>
    <div class="org-tagline">Transgender resource</div>

    <div class="contact-person">
      <div class="person-name">Marlene Osterby</div>
      <div class="person-title">president</div>
    </div>

    <div class="contact-line phone">
      <span>208 555 0147</span>
      <svg class="contact-icon" viewBox="0 0 28 28" aria-hidden="true">
        <rect width="28" height="28" fill="var(--band-black)"/>
        <path d="M6 10 q8 -5 16 0 v3 h-4 v-2 h-8 v2 h-4z M9 14 h10 l2 7 h-14z" fill="var(--white)"/>
        <circle cx="14" cy="17.5" r="2" fill="var(--band-black)"/>
      </svg>
    </div>

    <div class="contact-line address">
      <span>412 Pine Hollow mill rd. Ashford ne18532 suite 346</span>
      <svg class="contact-icon" viewBox="0 0 28 28" aria-hidden="true">
        <rect width="28" height="28" fill="var(--band-black)"/>
        <path d="M14 5 a7 7 0 0 1 7 7 c0 5 -7 11 -7 11 s-7 -6 -7 -11 a7 7 0 0 1 7 -7z" fill="var(--white)"/>
        <circle cx="14" cy="12" r="2.6" fill="var(--band-black)"/>
      </svg>
    </div>
  </div>
</body>
</html>
```